Webdesign für Gemeinschaftspraxis (13820)
Zielgruppe
Die Website ist für eine fachärztliche Gemeinschaftspraxis, die sich aus Internisten, Betriebsmedizinern, Präventionsärzten, Kardiologen, Allgemeinmedizinern und Phlebologen zusammensetzt.
Die Zielgruppe sind bestehende Patienten sowie potentielle Patienten.
Die Website soll informativ sein.
Aufgabenstellung
Die Website soll in schlichten Farben gehalten sein, die zum Logo und zu den Fotos passen.
Die Website soll als kurzer, informativer Auftritt dienen
Die gelieferten Fotos sollen verwendet werden.
Es soll eine Onepage-Website werden, die so aufgebaut ist, wie die Website unter dem folgenden Link: https://www.kolbenfeld-portal.de/

```html
<!DOCTYPE html>
<html lang="de">
<head>
<meta charset="utf-8">
<title>Leistungen – Praxis am Lindenhof</title>
<link rel="stylesheet" href="https://fonts.googleapis.com/css2?family=Fira+Sans:wght@400;500&family=Roboto:wght@400&display=swap">
<style>
  :root {
    --page-bg: #e4e4e4;
    --header-bg: #ffffff;
    --ink: #111111;
    --brand: #18203c;
    --panel-bg: #ffffff;
    --bar-bg: #535353;
    --bar-text: #ffffff;
    --heading-text: #4a4a4a;
    --body-text: #8a8a8a;
  }
  * { box-sizing: border-box; margin: 0; padding: 0; }
  html, body { width: 1200px; height: 793px; overflow: hidden; }
  body { background: var(--page-bg); font-family: "Roboto", Arial, sans-serif; position: relative; }

  .site-header {
    position: absolute; left: 0; top: 0; width: 1200px; height: 51px;
    background: var(--header-bg);
    box-shadow: 0 4px 14px rgba(0,0,0,0.06);
  }
  .brand {
    position: absolute; left: 228px; top: 11px; width: 100px;
    display: flex; align-items: center; gap: 5px;
    font-family: "Fira Sans", sans-serif; font-weight: 500; font-size: 11px;
    line-height: 13px; color: var(--brand);
  }
  .brand-square { flex: none; width: 10px; height: 10px; background: var(--brand); }
  .brand-name { display: block; }
  .main-nav { position: absolute; top: 15px; left: 0; }
  .nav-link {
    position: absolute; top: 0; height: 19px; line-height: 19px;
    font-size: 8px; letter-spacing: 0.3em; color: var(--ink); white-space: nowrap;
  }
  .nav-link.is-active {
    border: 1.2px solid var(--ink); width: 83px; text-align: center; line-height: 17px;
  }

  .page-title {
    position: absolute; left: 198px; top: 92px;
    font-weight: 400; font-size: 16px; letter-spacing: 0.12em; color: var(--ink);
  }

  .service-list {
    position: absolute; left: 198px; top: 125px; width: 558px;
    background: var(--panel-bg); list-style: none;
  }
  .service-open { height: 118px; padding: 7px 8px 0; }
  .service-open h2 {
    font-family: "Fira Sans", sans-serif; font-weight: 400; font-size: 10px;
    letter-spacing: 0.08em; color: var(--heading-text);
  }
  .service-open p {
    margin-top: 8px; width: 466px; font-size: 9.2px; line-height: 13.8px; color: var(--body-text);
  }
  .service-bar {
    height: 24.6px; margin: 0 1px 1.4px; background: var(--bar-bg);
    padding-left: 7px; line-height: 24.6px;
    font-family: "Fira Sans", sans-serif; font-size: 10px; letter-spacing: 0.09em;
    color: var(--bar-text); white-space: nowrap;
  }
  .service-bar:last-child { margin-bottom: 0; }
</style>
</head>
<body>
  <header class="site-header">
    <div class="brand"><span class="brand-square"></span><span class="brand-name">Praxis am<br>Lindenhof</span></div>
    <nav class="main-nav">
      <span class="nav-link" style="left:348px">Praxis</span>
      <span class="nav-link is-active" style="left:416px">Leistungen</span>
      <span class="nav-link" style="left:533px">Ärzte</span>
      <span class="nav-link" style="left:603px">Teams</span>
      <span class="nav-link" style="left:678px">Öffnungszeiten</span>
      <span class="nav-link" style="left:808px">Kontakt</span>
    </nav>
  </header>

  <h1 class="page-title">Leistungen</h1>

  <ul class="service-list">
    <li class="service-open">
      <h2>Gesundheitsvorsorge/Prävention/ Gesundheits-Check-up</h2>
      <p>Sed velit congue viverra. Sed porta mattis luctus. Curabitur feugiat pharetra sem eu iaculis. Phasellus venenatis volutpat arcu id placerat. Aliquam fringilla ligula eu purus lacinia at volutpat nunc malesuada. Nunc a augue ac orci tempus commodo. Sed velit congue viverra. Sed porta mattis luctus. Curabitur feugiat pharetra sem eu iaculis. Phasellus venenatis volutpat arcu id placerat. Aliquam fringilla ligula eu purus lacinia at volutpat nunc malesuada. Nunc a augue ac orci tempus commodo.</p>
    </li>
    <li class="service-bar">Impfungen und Reiseimpfungen</li>
    <li class="service-bar">Männervorsorge</li>
    <li class="service-bar">Diabetes mellitus</li>
    <li class="service-bar">Psychosomatische Grundversorgung</li>
    <li class="service-bar">Koronare Herzerkrankung (KHK)</li>
    <li class="service-bar">Asthma Bronchiale</li>
    <li class="service-bar">Palliativversorgung</li>
    <li class="service-bar">Prävention</li>
    <li class="service-bar">Echokardiografie</li>
    <li class="service-bar">Sonographische Untersuchung der Schilddrüse</li>
    <li class="service-bar">Check-up“-Laboruntersuchungen sowie PSA-Wert und andere Tumormarker</li>
    <li class="service-bar">EKG und Belastungs-EKG</li>
    <li class="service-bar">Langzeit-Blutdruckmessung</li>
    <li class="service-bar">Lungenfunktionstest</li>
    <li class="service-bar">Disease-Management-Programme (DMP)</li>
    <li class="service-bar">Ultraschall der Bauchorgane</li>
    <li class="service-bar">Ultraschall der Hirnversorgenden Arterien (Duplexsonografie)</li>
    <li class="service-bar">Spiroergometrie</li>
  </ul>
</body>
</html>
```